Original catchy book cover

I need a book cover for my book "The Steady Harbor Manual" (https://quillpress.example/harbormanual). This will be a book self published on brightmart.
The book talks about the following concepts:
- Iterative product delivery
- Early discovery using feedback from customers
- Start small, think big, move fast
- Slice the product into valuable increments that can be validated with customers
- Experimental approach to deciding the next slice of work
A simple cover that stands out from the business books already out there! Some examples are:
https://www.brightmart.example/Field-Notes-Thriving-Teams-Steadily-ebook/dp/Q00XTR4KWZ/ref=sr_1_1?ie=UTF8&qid=1500000001&sr=8-1&keywords=field+notes
https://www.brightmart.example/Quiet-Harbor-Almanac-Shape-Offerings-ebook/dp/Q00MVK219J/ref=sr_1_1?s=digital-text&ie=UTF8&qid=1500000002&sr=1-1&keywords=quiet+harbor+almanac
https://www.brightmart.example/Course-Charts-Renewed-Heading-Fog-ebook/dp/Q099WT71ZD/ref=pd_sim_351_2?_encoding=UTF8&psc=1&refRID=9QZTRWJDDAV52LM0NKPP
Lastly, attached are 2 draft covers that i've been playing with. Would love a graphic as part of the cover if it makes sense in your design! The graphic should tie to the meaning or themes of the book. Emphasis on ways of working, collaboration, experimentation, hypothesis, agile, incremental or adaptive. Those are some words that describe the content of the book.
Alternatively, something abstract could also be an option if a literal graphic doesn't suit the theme of your design.
Target Market(s)
Product owners, scrum masters, people in the agile community, software developers, designers
Industry/Entity Type
Information Technology
Font styles to use
Colors
Designer to choose colors to be used in the design.
Requirements
Must have
- Title, Subtitle, Author Name
- Back of the book should have space for a description (use lorem ipsum for now)
- Please use the editorial logo
- (please omit "created by Tomas Verlindt" because the editorial logo replaces that.
- The design must be original art or graphics (i.e. it should be similar to another cover in this topic).
Nice to have
- A graphic would be ideal if it is relevant to the book topic, otherwise a nice simple cover that uses colors or patterns that are easy to recall.
- The color suggestions below are suggestions only. Do not feel you have to incorporate all the colors and feel free to recommend an alternate palette.
Should not have
- Clipart or generic stock art photos. Images for the sake of images, traditional logos (e.g. a computer, a phone etc unless it's part of an overall theme that ties the logos together).

```html
<!DOCTYPE html>
<html lang="en">
<head>
<meta charset="utf-8">
<title>The Steady Harbor Manual — Cover Front and Back</title>
<link rel="stylesheet" href="https://fonts.googleapis.com/css2?family=Roboto:ital,wght@0,100;0,300;0,400;0,500;0,700;0,900;1,500&display=swap">
<style>
  :root {
    --purple-deep: #4e0840;
    --purple-mid: #8a2a74;
    --purple-glow: #a23a88;
    --gold: #f0ae1c;
    --magenta: #b8207f;
    --white: #ffffff;
    --ink: #2a2a2e;
    --publisher: #e8602a;
    --stage-light: #d6d4d4;
    --stage-dark: #858180;
  }
  * { box-sizing: border-box; margin: 0; padding: 0; }
  html, body { width: 1200px; height: 1034px; overflow: hidden; }
  body {
    font-family: "Roboto", Arial, sans-serif;
    background: radial-gradient(ellipse 520px 460px at 640px 320px, var(--stage-light), var(--stage-dark) 100%);
    position: relative;
  }
  .side-label {
    position: absolute;
    font-weight: 700;
    font-size: 25px;
    color: var(--ink);
    transform: translateX(-50%);
    letter-spacing: 0.5px;
  }
  .side-label--front { left: 347px; top: 33px; }
  .side-label--back { left: 865px; top: 288px; }

  .cover {
    position: absolute;
    overflow: hidden;
    box-shadow: 0 14px 40px rgba(0,0,0,0.45);
    background: var(--white);
  }
  .cover--front { left: 88px; top: 90px; width: 518px; height: 671px; }
  .cover--back { left: 623px; top: 346px; width: 487px; height: 630px; }
  .cover__art { position: absolute; inset: 0; }
  .cover__text { position: absolute; left: 0; right: 0; text-align: center; }

  /* Title lockup */
  .title-lockup { position: absolute; inset: 0; }
  .title-lockup__frame { position: absolute; inset: 0; }
  .title-lockup__top {
    position: absolute; left: 0; right: 0; text-align: center;
    color: var(--white); font-weight: 100; line-height: 1;
  }
  .title-lockup__main {
    position: absolute; left: 0; right: 0; text-align: center;
    color: var(--gold); font-weight: 900; line-height: 1; letter-spacing: 1px;
  }
  .title-lockup__tag {
    position: absolute; background: var(--white); border-radius: 6px;
    color: var(--purple-deep); font-weight: 300; line-height: 1;
    display: flex; align-items: center; justify-content: center;
  }

  .subtitle { color: var(--magenta); font-weight: 700; letter-spacing: -0.3px; }
  .author { color: var(--magenta); font-weight: 700; }
  .blurb { color: var(--white); font-style: italic; font-weight: 500; text-align: left; }

  .publisher {
    position: absolute; display: flex; align-items: center;
    color: var(--publisher); font-weight: 400; line-height: 1.05;
  }
  .publisher__dot { border-radius: 50%; background: var(--publisher); flex: none; }
  .publisher__url { display: block; }
</style>
</head>
<body>

<div class="side-label side-label--front">FRONT</div>
<div class="side-label side-label--back">BACK</div>

<!-- FRONT COVER -->
<section class="cover cover--front">
  <svg class="cover__art" width="518" height="671" viewBox="0 0 518 671" role="img" aria-label="Purple panel with soft diagonal texture, gold corner bands">
    <defs>
      <radialGradient id="frontGlow" cx="0.5" cy="0.4" r="0.7">
        <stop offset="0" stop-color="#a23a88"/>
        <stop offset="1" stop-color="#4e0840"/>
      </radialGradient>
      <linearGradient id="frontBar" x1="0" x2="1">
        <stop offset="0" stop-color="#4e0840"/>
        <stop offset="0.5" stop-color="#a23a88"/>
        <stop offset="1" stop-color="#4e0840"/>
      </linearGradient>
    </defs>
    <rect x="0" y="0" width="518" height="22" fill="#f0ae1c"/>
    <polygon points="0,20 259,0 518,20 518,356 0,385" fill="url(#frontGlow)"/>
    <line x1="0" y1="385" x2="518" y2="356" stroke="#b8207f" stroke-width="3"/>
    <rect x="0" y="600" width="518" height="40" fill="#f0ae1c"/>
    <polygon points="0,601 259,630 518,601 518,613 259,632 0,613" fill="#4e0840"/>
    <polygon points="0,590 518,590 518,601 259,630 0,601" fill="#ffffff"/>
    <rect x="0" y="633" width="518" height="38" fill="url(#frontBar)"/>
  </svg>

  <div class="title-lockup">
    <svg class="title-lockup__frame" width="518" height="671" viewBox="0 0 518 671" aria-hidden="true">
      <path d="M86,147 H68 Q60,147 60,155 V269 Q60,277 68,277 H450 Q458,277 458,269 V155 Q458,147 450,147 H432" fill="none" stroke="#ffffff" stroke-width="2"/>
    </svg>
    <div class="title-lockup__top" style="top:110px; font-size:58px;">THE STEADY</div>
    <div class="title-lockup__main" style="top:168px; font-size:86px;">HARBOR</div>
    <div class="title-lockup__tag" style="left:143px; top:251px; width:232px; height:50px; font-size:50px;">MANUAL</div>
  </div>

  <div class="cover__text subtitle" style="top:396px; font-size:24px; line-height:30px;">A practitioner’s guide to building viable<br>products customers love.</div>
  <div class="cover__text author" style="top:499px; font-size:31px;">Dara Vohn</div>

  <div class="publisher" style="left:197px; top:562px; font-size:16px;">
    <span class="publisher__dot" style="width:38px; height:38px; margin-right:10px;"></span>
    <span>Editora<br>Solvane<span class="publisher__url" style="font-size:11px;">solvane.org</span></span>
  </div>
</section>

<!-- BACK COVER -->
<section class="cover cover--back">
  <svg class="cover__art" width="487" height="630" viewBox="0 0 487 630" role="img" aria-label="Purple panel with soft diagonal texture, gold corner bands">
    <defs>
      <radialGradient id="backGlow" cx="0.5" cy="0.45" r="0.7">
        <stop offset="0" stop-color="#a23a88"/>
        <stop offset="1" stop-color="#4e0840"/>
      </radialGradient>
      <linearGradient id="backBar" x1="0" x2="1">
        <stop offset="0" stop-color="#4e0840"/>
        <stop offset="0.5" stop-color="#a23a88"/>
        <stop offset="1" stop-color="#4e0840"/>
      </linearGradient>
    </defs>
    <rect x="0" y="0" width="487" height="20" fill="#f0ae1c"/>
    <polygon points="0,18 243,0 487,18 487,361 0,336" fill="url(#backGlow)"/>
    <line x1="0" y1="336" x2="487" y2="361" stroke="#b8207f" stroke-width="3"/>
    <rect x="0" y="565" width="487" height="35" fill="#f0ae1c"/>
    <polygon points="0,567 243,593 487,567 487,578 243,594 0,578" fill="#4e0840"/>
    <polygon points="0,555 487,555 487,567 243,593 0,567" fill="#ffffff"/>
    <rect x="0" y="595" width="487" height="35" fill="url(#backBar)"/>
  </svg>

  <div class="title-lockup">
    <svg class="title-lockup__frame" width="487" height="630" viewBox="0 0 487 630" aria-hidden="true">
      <path d="M173,52 H169 Q164,52 164,57 V101 Q164,106 169,106 H318 Q323,106 323,101 V57 Q323,52 318,52 H314" fill="none" stroke="#ffffff" stroke-width="1.5"/>
    </svg>
    <div class="title-lockup__top" style="top:33px; font-size:23px;">THE STEADY</div>
    <div class="title-lockup__main" style="top:62px; font-size:36px;">HARBOR</div>
    <div class="title-lockup__tag" style="left:195px; top:95px; width:97px; height:20px; font-size:20px; border-radius:4px;">MANUAL</div>
  </div>

  <p class="cover__text blurb" style="left:53px; right:36px; top:144px; font-size:14.6px; line-height:19.2px;">Lorem ipsum dolor sit amet, exerci omittantur liberavisse cu mei, te usu velit nominati mediocrem, et vis omnis rebum instructior. Ut usu novum omnes, solet mollis suavitate eu vis. Sit ad verterem vulputate cotidieque, elit dicant sapientem ne quo. Nec cu explicari scriptorem comprehensam, epicurei luptatum ea vim, et aperiri debitis omittantur his. Dico possit latine in vim. Ex ius ipsum congue iudico.</p>

  <div class="cover__text subtitle" style="top:371px; font-size:23px; line-height:28px;">A practitioner’s guide to building viable<br>products customers love.</div>
  <div class="cover__text author" style="top:484px; font-size:26px;">Dara Vohn</div>

  <div class="publisher" style="left:204px; top:543px; font-size:11.5px;">
    <span class="publisher__dot" style="width:28px; height:28px; margin-right:7px;"></span>
    <span>Editora<br>Solvane<span class="publisher__url" style="font-size:8px;">solvane.org</span></span>
  </div>
</section>

</body>
</html>
```